Velmont perks circle

We are looking to redesign the user interface of our mobile app “Velmont Perks”, which is the official rewards program for our luxury casino brand, Orvantis Colombo.
Our goal is to give the app a more elegant, premium, and user-friendly design that reflects the exclusivity of our brand and the luxury experience we offer our VIP clientele.
What We Need:
A complete UI design for the app’s main screens, including:
Splash Screen
01 Login / Signup Screen
02 Home Dashboard
Buttons -
Home / my card / my wallet / my booking / my host
My wallet / my offer / lucky game / my taxi / entertainment / online
03 Profile screen
04 My wallet
05 My offer
06Packages
07 My booking
08 My host
09 My card
we attached our privies app all the screen for you reference
Inspiration:
Think of luxury brands like Hadley-Voss, Corvix Sapphire, or high-end lifestyle apps. Clean interfaces, classy animations, and a sense of exclusivity are key.
We’re excited to see fresh, innovative takes that elevate the app to a truly world-class luxury experience for our users.
Thank you!

```html
<!DOCTYPE html>
<html lang="en">
<head>
<meta charset="utf-8">
<title>Velmont Perks – App Screens</title>
<link href="https://fonts.googleapis.com/css2?family=Arimo:wght@400;700&display=swap" rel="stylesheet">
<style>
:root{
  --bg:#3a2a1e;
  --bg-low:#2a1f17;
  --gold:#f0a020;
  --gold-soft:#d4891e;
  --screen-top:#070403;
  --screen-mid:#2a1a0e;
  --panel-red:#6e1c12;
  --panel-red-dark:#3e0e0a;
  --text:#ffffff;
  --muted:#e9dcd0;
  --link:#ff3b2f;
  --tile:#0c0806;
}
*{box-sizing:border-box;margin:0;padding:0}
html,body{width:1200px;height:793px;overflow:hidden}
body{background:linear-gradient(var(--bg) 0 61%,var(--bg-low) 61% 100%);font-family:"Arimo",Arial,sans-serif;color:var(--text);position:relative}
.screen{position:absolute;top:87px;width:276px;height:608px;border-radius:24px;overflow:hidden;
  background:linear-gradient(180deg,var(--screen-top) 0%,var(--screen-mid) 48%,#140c06 100%)}
.screen--login{left:99px;background:linear-gradient(180deg,#0b0605 0%,#1a0b07 50%,#050303 100%)}
.screen--home{left:463px}
.screen--gaming{left:825px}
.abs{position:absolute}

/* brand */
.brand{left:0;right:0;top:30px;display:flex;flex-direction:column;align-items:center;gap:6px}
.brand__mark{width:26px;height:26px;border-radius:50%;background:#d63a25}
.brand__name{font-weight:700;font-size:17px;color:var(--gold);text-align:center;line-height:1.2;letter-spacing:.5px}

/* login panel */
.auth{left:26px;top:143px;width:225px;height:394px;border-radius:44px;border:2px solid var(--gold);
  box-shadow:0 0 10px rgba(240,160,32,.55);background:linear-gradient(180deg,var(--panel-red) 0%,#5a150e 60%,var(--panel-red-dark) 100%);
  display:flex;flex-direction:column;align-items:center;padding-top:28px;text-align:center}
.auth__title{font-weight:700;font-size:12.5px}
.auth__text{font-size:10.3px;line-height:15px;color:var(--muted);margin-top:6px;width:170px}
.auth__btn{margin-top:12px;height:30px;border:1.5px solid var(--gold);border-radius:16px;background:linear-gradient(#8a2416,#5c140c);
  font-weight:700;font-size:10.5px;letter-spacing:.5px;display:flex;align-items:center;justify-content:center;padding:0 20px}
.auth__gap{margin-top:26px}
.auth__or{margin-top:15px;font-weight:700;font-size:12px}

/* status & header */
.status{left:20px;right:22px;top:17px;display:flex;justify-content:space-between;align-items:center;font-weight:700;font-size:12px}
.status__icons{display:flex;gap:6px;align-items:center}
.topbar{left:0;right:0;top:46px;height:39px;border-top:2px solid var(--gold);border-bottom:2px solid var(--gold);
  background:#0a0604;display:flex;align-items:center;justify-content:space-between;padding:0 18px 0 19px}
.topbar__title{font-weight:700;font-size:12px;color:var(--gold);letter-spacing:.5px}
.bell{position:relative}
.bell__count{position:absolute;top:-6px;right:-5px;width:9px;height:9px;border-radius:50%;background:#e0261b;font-size:6.5px;
  display:flex;align-items:center;justify-content:center}

/* hero */
.hero{left:44px;top:101px;width:188px;height:188px;border-radius:50%;
  background:radial-gradient(circle,#8a5a2a 0%,#5a3a1a 55%,#9a6a1c 78%,#3a240f 100%);box-shadow:0 0 0 4px #6a4512}

/* tiles */
.tile{width:57px;display:flex;flex-direction:column;align-items:center}
.tile__box{width:57px;height:57px;border:1px solid #e5d7c5;border-radius:5px;background:var(--tile);display:flex;align-items:center;justify-content:center}
.tile__label{margin-top:7px;font-size:9.8px;color:var(--muted);white-space:nowrap}

/* bottom nav */
.nav{left:0;right:0;bottom:0;height:54px}
.nav__line{left:0;top:0}
.nav__fab{left:117px;top:-20px;width:42px;height:42px;border-radius:50%;background:#3a2410;display:flex;align-items:center;justify-content:center}
.nav__items{left:0;right:0;top:10px;display:flex;justify-content:space-around;padding:0 4px}
.nav__item{width:50px;display:flex;flex-direction:column;align-items:center;gap:4px;font-size:6.5px;color:var(--muted)}
.nav__item--blank svg{visibility:hidden}

/* game list */
.game{left:18px;right:22px;height:106px;border-bottom:1px solid #3c2a1c}
.game:last-of-type{border-bottom:none}
.game__thumb{left:0;top:2px;width:48px;height:48px;border-radius:50%;border:2.5px solid #b8781c;background:linear-gradient(135deg,#5a3a22,#1e3a2a)}
.game__title{left:56px;top:6px;font-weight:700;font-size:12.5px;color:var(--gold);letter-spacing:.4px}
.game__text{left:56px;top:23px;width:180px;font-size:9.3px;line-height:11.8px;color:var(--muted)}
.game__link{left:56px;top:69px;font-size:9.3px;color:var(--link);text-decoration:underline}
</style>
</head>
<body>

<svg width="0" height="0" style="position:absolute">
  <defs>
    <symbol id="i-wallet" viewBox="0 0 24 24"><path d="M3 6h15v3h3v10H3z" fill="currentColor"/><rect x="13" y="11" width="8" height="5" rx="1" fill="#000" opacity=".45"/><circle cx="16" cy="13.5" r="1.2" fill="currentColor"/></symbol>
    <symbol id="i-home" viewBox="0 0 24 24"><path d="M3 11 12 3l9 8v10h-6v-6H9v6H3z" fill="currentColor"/></symbol>
    <symbol id="i-card" viewBox="0 0 24 24"><rect x="2" y="5" width="20" height="14" rx="2" fill="currentColor"/><rect x="2" y="8.5" width="20" height="2.5" fill="#000" opacity=".45"/></symbol>
    <symbol id="i-booking" viewBox="0 0 24 24"><rect x="3" y="5" width="18" height="16" rx="2" fill="currentColor"/><rect x="7" y="2" width="2" height="5" fill="currentColor"/><rect x="15" y="2" width="2" height="5" fill="currentColor"/><path d="M8 14l3 3 5-6" stroke="#000" stroke-opacity=".5" stroke-width="2" fill="none"/></symbol>
    <symbol id="i-host" viewBox="0 0 24 24"><rect x="3" y="3" width="18" height="5" rx="1" fill="currentColor"/><rect x="3" y="10" width="18" height="5" rx="1" fill="currentColor"/><rect x="3" y="17" width="18" height="5" rx="1" fill="currentColor"/></symbol>
    <symbol id="i-menu" viewBox="0 0 24 24"><rect x="3" y="5" width="18" height="3" fill="currentColor"/><rect x="3" y="11" width="18" height="3" fill="currentColor"/><rect x="3" y="17" width="18" height="3" fill="currentColor"/></symbol>
    <symbol id="i-bell" viewBox="0 0 24 24"><path d="M12 3c-4 0-6 3-6 7v5l-2 3h16l-2-3v-5c0-4-2-7-6-7z" fill="currentColor"/><circle cx="12" cy="20.5" r="2" fill="currentColor"/></symbol>
    <symbol id="i-status" viewBox="0 0 80 14">
      <rect x="0" y="10" width="2.5" height="3" fill="#fff"/><rect x="4" y="7.5" width="2.5" height="5.5" fill="#fff"/><rect x="8" y="5" width="2.5" height="8" fill="#fff"/><rect x="12" y="2" width="2.5" height="11" fill="#fff"/>
      <path d="M26 5a10 10 0 0 1 14 0l-2 2a7 7 0 0 0-10 0zM29.5 8.5a5 5 0 0 1 7 0L33 12z" fill="#fff"/>
      <rect x="52" y="2" width="17" height="10" rx="2" stroke="#fff" stroke-width="1.4" fill="none"/><rect x="54" y="4" width="11" height="6" fill="#fff"/><rect x="70" y="5" width="1.8" height="4" fill="#fff"/>
    </symbol>
  </defs>
</svg>

<!-- Login screen -->
<section class="screen screen--login">
  <div class="abs brand">
    <span class="brand__mark"></span>
    <span class="brand__name">VELMONT PERKS<br>CIRCLE</span>
  </div>
  <div class="abs auth">
    <h2 class="auth__title">Member Login</h2>
    <p class="auth__text">Lorem ipsum dolor sit amet, consec tetur adipiscing elit</p>
    <div class="auth__btn">SIGN IN</div>
    <h2 class="auth__title auth__gap">New Member Login</h2>
    <p class="auth__text">Lorem ipsum dolor sit amet, consec tetur adipiscing elit</p>
    <div class="auth__btn">SIGN UP</div>
    <p class="auth__or">(or)</p>
    <p class="auth__text">Lorem ipsum dolor sit amet, consec tetur adipiscing elit</p>
    <div class="auth__btn">TEMPORARY SIGN UP</div>
  </div>
</section>

<!-- Home dashboard -->
<section class="screen screen--home">
  <div class="abs status"><span>9.41</span><svg width="56" height="11"><use href="#i-status"/></svg></div>
  <header class="abs topbar">
    <svg width="13" height="13" style="color:var(--gold)"><use href="#i-menu"/></svg>
    <span class="bell"><svg width="14" height="14" style="color:var(--gold)"><use href="#i-bell"/></svg><span class="bell__count">0</span></span>
  </header>
  <div class="abs hero" role="img" aria-label="Slot machine reels with lucky sevens surrounded by dice"></div>

  <div class="abs tile" style="left:20px;top:310px"><div class="tile__box" style="color:var(--gold)"><svg width="26" height="26"><use href="#i-wallet"/></svg></div><span class="tile__label">My Wallet</span></div>
  <div class="abs tile" style="left:108px;top:310px"><div class="tile__box"><svg width="26" height="26" viewBox="0 0 24 24"><path d="M12 2l2.5 2 3-.5 1 3 2.5 2-1.5 2.5 1.5 2.5-2.5 2-1 3-3-.5L12 22l-2.5-2-3 .5-1-3L3 15.5 4.5 13 3 10.5l2.5-2 1-3 3 .5z" fill="var(--gold)"/><path d="M8.5 15.5l7-7" stroke="#000" stroke-width="1.6"/><circle cx="9" cy="9" r="1.4" fill="#000"/><circle cx="15" cy="15" r="1.4" fill="#000"/></svg></div><span class="tile__label">My Offer</span></div>
  <div class="abs tile" style="left:196px;top:310px"><div class="tile__box"><svg width="26" height="26" viewBox="0 0 24 24"><path d="M6 7h12a4 4 0 0 1 4 4v5a3 3 0 0 1-5 2l-2-2H9l-2 2a3 3 0 0 1-5-2v-5a4 4 0 0 1 4-4z" fill="var(--gold)"/><path d="M6 12h4M8 10v4" stroke="#000" stroke-width="1.6"/><circle cx="16" cy="11" r="1.1" fill="#000"/><circle cx="18" cy="13.5" r="1.1" fill="#000"/></svg></div><span class="tile__label">Lucky Game</span></div>
  <div class="abs tile" style="left:20px;top:398px"><div class="tile__box"><svg width="26" height="26" viewBox="0 0 24 24"><rect x="9" y="3" width="6" height="3" fill="var(--gold)"/><path d="M6 7h12l2 5h1v6h-2v2h-3v-2H8v2H5v-2H3v-6h1z" fill="var(--gold)"/><path d="M7 9h10l1.2 3H5.8z" fill="#000"/><circle cx="7" cy="15" r="1.3" fill="#000"/><circle cx="17" cy="15" r="1.3" fill="#000"/></svg></div><span class="tile__label">My Taxi</span></div>
  <div class="abs tile" style="left:108px;top:398px"><div class="tile__box"><svg width="26" height="26" viewBox="0 0 24 24"><path d="M2 7c3 1 6 1 9 0v6a4.5 4.5 0 0 1-9 0z" fill="var(--gold)"/><path d="M12 4c3 1 7 1 10 0v6a5 5 0 0 1-10 0z" fill="var(--gold-soft)"/><path d="M4 14q2.5 2 5 0" stroke="#000" stroke-width="1.2" fill="none"/><path d="M14.5 12q2.5-2 5 0" stroke="#000" stroke-width="1.2" fill="none"/></svg></div><span class="tile__label">Entertainment</span></div>
  <div class="abs tile" style="left:196px;top:398px"><div class="tile__box"><svg width="26" height="26" viewBox="0 0 24 24"><circle cx="12" cy="6" r="3.5" fill="var(--gold)"/><path d="M5 15q0-5 7-5t7 5z" fill="var(--gold)"/><rect x="4" y="15" width="16" height="7" rx="1" fill="var(--gold)"/><circle cx="12" cy="18.5" r="1.2" fill="#000"/></svg></div><span class="tile__label">Online</span></div>

  <nav class="abs nav">
    <svg class="abs nav__line" width="276" height="54"><path d="M0 1H110l22 16h12l22-16H276" stroke="var(--gold)" stroke-width="2" fill="none"/><path d="M0 2H110l22 16h12l22-16H276V54H0z" fill="#1a0f07"/></svg>
    <div class="abs nav__fab" style="color:var(--gold)"><svg width="16" height="16"><use href="#i-wallet"/></svg></div>
    <div class="abs nav__items">
      <div class="nav__item"><svg width="16" height="16" style="color:var(--gold-soft)"><use href="#i-home"/></svg>Home</div>
      <div class="nav__item"><svg width="16" height="16" style="color:var(--gold-soft)"><use href="#i-card"/></svg>My Card</div>
      <div class="nav__item nav__item--blank"><svg width="16" height="16"><use href="#i-wallet"/></svg>My Wallet</div>
      <div class="nav__item"><svg width="16" height="16" style="color:var(--gold-soft)"><use href="#i-booking"/></svg>My Booking</div>
      <div class="nav__item"><svg width="16" height="16" style="color:var(--gold-soft)"><use href="#i-host"/></svg>My Host</div>
    </div>
  </nav>
</section>

<!-- Gaming screen -->
<section class="screen screen--gaming">
  <div class="abs status"><span>9.41</span><svg width="56" height="11"><use href="#i-status"/></svg></div>
  <header class="abs topbar">
    <svg width="13" height="13" style="color:var(--gold)"><use href="#i-menu"/></svg>
    <span class="topbar__title">GAMING</span>
    <span class="bell"><svg width="14" height="14" style="color:var(--gold)"><use href="#i-bell"/></svg><span class="bell__count">0</span></span>
  </header>

  <article class="abs game" style="top:108px">
    <div class="abs game__thumb" role="img" aria-label="Baccarat table with dealer's hands and cards"></div>
    <h3 class="abs game__title">BACCARAT</h3>
    <p class="abs game__text">Lorem ipsum dolor sit amet, consectetur adipiscing elit, sed do eiusmod tempor incididunt ut labore et dolore</p>
    <span class="abs game__link">View More</span>
  </article>
  <article class="abs game" style="top:214px">
    <div class="abs game__thumb" role="img" aria-label="Roulette wheel and betting table"></div>
    <h3 class="abs game__title">ROULETTE</h3>
    <p class="abs game__text">Lorem ipsum dolor sit amet, consectetur adipiscing elit, sed do eiusmod tempor incididunt ut labore et dolore</p>
    <span class="abs game__link">View More</span>
  </article>
  <article class="abs game" style="top:319px">
    <div class="abs game__thumb" role="img" aria-label="Blackjack cards and chips"></div>
    <h3 class="abs game__title">BLACKJACK</h3>
    <p class="abs game__text">Lorem ipsum dolor sit amet, consectetur adipiscing elit, sed do eiusmod tempor incididunt ut labore et dolore</p>
    <span class="abs game__link">View More</span>
  </article>
  <article class="abs game" style="top:425px">
    <div class="abs game__thumb" role="img" aria-label="Fanned playing cards on green felt"></div>
    <h3 class="abs game__title">SABONG CARDS</h3>
    <p class="abs game__text">Lorem ipsum dolor sit amet, consectetur adipiscing elit, sed do eiusmod tempor incididunt ut labore et dolore</p>
    <span class="abs game__link">View More</span>
  </article>

  <nav class="abs nav">
    <svg class="abs nav__line" width="276" height="54"><path d="M0 1H110l22 16h12l22-16H276" stroke="var(--gold)" stroke-width="2" fill="none"/><path d="M0 2H110l22 16h12l22-16H276V54H0z" fill="#1a0f07"/></svg>
    <div class="abs nav__fab" style="color:var(--gold)"><svg width="16" height="16"><use href="#i-wallet"/></svg></div>
    <div class="abs nav__items">
      <div class="nav__item"><svg width="16" height="16" style="color:var(--gold-soft)"><use href="#i-home"/></svg>Home</div>
      <div class="nav__item"><svg width="16" height="16" style="color:var(--gold-soft)"><use href="#i-card"/></svg>My Card</div>
      <div class="nav__item nav__item--blank"><svg width="16" height="16"><use href="#i-wallet"/></svg>My Wallet</div>
      <div class="nav__item"><svg width="16" height="16" style="color:var(--gold-soft)"><use href="#i-booking"/></svg>My Booking</div>
      <div class="nav__item"><svg width="16" height="16" style="color:var(--gold-soft)"><use href="#i-host"/></svg>My Host</div>
    </div>
  </nav>
</section>

</body>
</html>
```